Design for company homepage promoting to the pharmaceutical industry

Our company produces medical education materials and services for the pharmaceutical industry. Our existing website (www.quorvane.net.au) provides more information.
 
We need a homepage design for our new company website we are creating. Our site will not have a great amount of content, we want it to be fast, user friendly and easily adaptable to viewing on any platform, and through any browser. We don't want it over-designed - i.e. no highly animated banner flags, backgrounds, obscure webfonts, too many graphics etc. Attached are files indicating our existing company logo and design. We want the logo and rings to be retained. We've also attached draft copy for the website.
The final website may be designed in Wordpress (still to be confirmed)
 
This is a design to replace the current site (www.quorvane.net.au). Content will also be revised.
Things we don't like about our current design - doesn't use our current branding, is not very exciting, old fashioned 'standard' format, too much content, just doesn't look that good, boring.
 
Examples of sites we like:
www.bralimo.com.au
http://factsheets.tenvoramed.com.au/index.html
 
Features we like from these sites - fast, responsive, short and to the point, cross-platform compatible including smartphones, and looks good
 
Main reasons people will visit our site: to find out whether we can provide services they might be looking for, to make a decision on whether they are interested in what we offer so they can get in touch with us, and to get our contact details.
Main thing we want to achieve from website visits is that it looks good enough and provides enough summary information on us so that they want to get in touch with us, to offer us work or to ask us to come in and meet them to provide more info on what we do.
Two most important calls to action from our website
· make the decision that we can do what you are looking for
· get in touch with us.
Updates

Thanks everyone for your submissions. At this stage with the Christmas break upon us, we are yet to finalise our decision, and will make a decision early in the new year. I hope everyone has a good holiday break.
Kind regards
Giles

Target Market(s)

Pharmaceutical industry professionals, marketers and medical professionals.

Industry/Entity Type

Pharmaceutical

Requirements
Must have
• Company logo and rings must be incorporated, company colour - blue - must be in there.
Should not have
• Complex animation or graphics that will slow the upload or limit cross-platform compatability/viewing on smartphones etc.

```html
<!DOCTYPE html>
<html lang="en">
<head>
<meta charset="utf-8">
<title>Quorvane Healthcare Education</title>
<link href="https://fonts.googleapis.com/css2?family=Arimo:wght@400;700&family=Poiret+One&display=swap" rel="stylesheet">
<style>
:root{
  --brand-blue:#1a5ea0;
  --ink:#111;
  --grey-text:#555;
  --light-grey-text:#9a9a9a;
  --cyan-start:#1cc0df;
  --cyan-end:#8fe7f6;
  --band-grey:#e4e4e4;
  --tab-bar:#d6d6d6;
  --panel-grey:#ececec;
  --tab-active:#1a5ea0;
  --accent-blue:#5aa9d6;
  --yellow:#ffd200;
  --footer:#242424;
  --white:#fff;
}
*{box-sizing:border-box;margin:0;padding:0}
html,body{width:1200px;height:2579px;overflow:hidden}
body{position:relative;background:var(--white);font-family:"Arimo",Arial,sans-serif;color:var(--ink)}
.abs{position:absolute}
.thin{font-family:"Poiret One",sans-serif}

/* header */
.site-header{left:0;top:0;width:1200px;height:216px;background:linear-gradient(#fff,#f6f8fa)}
.client-login{left:972px;top:0;width:143px;height:28px;background:var(--brand-blue);color:#fff;font-size:12px;font-weight:700;text-align:center;line-height:28px}
.logo{left:0;width:1200px;top:30px;text-align:center;color:var(--brand-blue);font-size:52px;letter-spacing:1px}
.main-nav{top:128px;left:0;width:1200px;font-size:16px;color:#000}
.main-nav span{position:absolute}

/* intro */
.intro{left:0;top:216px;width:1200px;height:229px;background:#fff;border-bottom:4px solid #ececec}
.intro h1{position:absolute;left:76px;top:22px;width:850px;white-space:nowrap;font-weight:400;font-size:23px;line-height:36px;color:#333;letter-spacing:.5px;text-transform:uppercase}
.intro p{position:absolute;left:76px;top:146px;width:860px;font-size:12px;line-height:16px;color:var(--light-grey-text);font-family:"Poiret One",sans-serif;text-transform:uppercase;letter-spacing:.3px}
.media{background:linear-gradient(135deg,#d8eef2,#2b8fa8 45%,#c8e4ea);border-radius:6px;box-shadow:0 0 4px rgba(0,0,0,.25)}

/* who we are */
.who{left:0;top:465px;width:1200px;height:560px;background:linear-gradient(90deg,var(--cyan-start),var(--cyan-end))}
.who h2{position:absolute;left:76px;top:32px;font-weight:400;font-size:32px;color:#000}
.who .team{position:absolute;left:76px;top:110px;font-size:12px;line-height:20px;text-transform:uppercase;color:#000}
.portrait{left:76px;top:197px;width:96px;height:88px;background:linear-gradient(#e9e9e9,#9a9a9a)}
.who .name{position:absolute;left:76px;top:303px;font-size:22px;color:#fff}
.who .role{position:absolute;left:76px;top:333px;font-size:12px;text-transform:uppercase}
.who .bio{position:absolute;left:76px;top:372px;width:460px;font-size:12px;line-height:20px}
.proud-rule{left:634px;width:456px;height:2px;background:#fff}
.proud{left:600px;width:524px;top:148px;text-align:center;color:#fff;font-size:58px;line-height:80px;text-transform:uppercase}

/* what we do */
.what{left:0;top:1025px;width:1200px;height:395px;background:var(--panel-grey)}
.what .top{position:absolute;left:0;top:0;width:1200px;height:115px;background:var(--band-grey)}
.what h2{position:absolute;left:84px;top:50px;font-weight:400;font-size:32px}
.tabs{position:absolute;left:0;top:115px;width:1200px;height:25px;background:var(--tab-bar);font-size:13px;color:var(--brand-blue)}
.tabs span{position:absolute;top:0;line-height:25px;padding:0 12px}
.tabs .active{background:var(--tab-active);color:#fff}
.what h3{position:absolute;left:0;width:1200px;top:203px;text-align:center;font-weight:400;font-size:28px;letter-spacing:3px;color:var(--accent-blue);font-family:"Poiret One",sans-serif}
.what p{position:absolute;left:150px;width:920px;top:250px;text-align:center;font-size:13px;line-height:22px;color:#555}

/* clients */
.clients h2{position:absolute;left:0;width:1200px;top:1468px;text-align:center;font-weight:400;font-size:32px}
.quotes{left:76px;top:1540px;width:800px;font-size:12px;line-height:17px;color:#555}
.quotes p{margin-bottom:12px}
.some{left:0;width:1200px;top:1720px;text-align:center;font-size:15px}
.client{font-size:16px;font-weight:700;color:var(--brand-blue);display:flex;align-items:center;gap:8px}
.client i{display:block;width:14px;height:14px;border-radius:50%;background:var(--brand-blue)}

/* join */
.join{left:0;top:1935px;width:1200px;height:135px;background:var(--yellow)}
.join h2{position:absolute;left:86px;top:28px;font-weight:400;font-size:31px;letter-spacing:1px}
.join .tag{position:absolute;left:218px;top:82px;color:#fff;font-size:21px}
.join .field{position:absolute;left:672px;top:80px;width:273px;height:31px;background:#fff;border:1px solid #ccc;font-size:13px;color:#bbb;line-height:29px;padding-left:8px}
.join .btn{position:absolute;left:945px;top:80px;width:102px;height:31px;background:#111;color:#fff;font-size:12px;font-weight:700;text-align:center;line-height:31px}

/* footer */
.footer{left:0;top:2070px;width:1200px;height:245px;background:var(--footer);color:#fff}
.footer h2{position:absolute;left:84px;top:26px;font-weight:400;font-size:33px;color:var(--brand-blue)}
.footer h4{position:absolute;font-weight:400;font-size:16px}
.footer .lines{position:absolute;font-size:12px;line-height:16px}
.social{position:absolute;top:98px;width:60px;text-align:center;font-size:9px}
.social i{display:block;margin:0 auto 10px;width:44px;height:44px;border-radius:50%;background:#fff}
.footer .small{position:absolute;top:213px;font-size:9px}
.map{left:0;top:2315px;width:1200px;height:264px;background:linear-gradient(135deg,#e6e6e6,#d4d4d4 50%,#e2e2e2)}
</style>
</head>
<body>

<header class="abs site-header">
  <div class="abs client-login">CLIENT LOGIN</div>
  <div class="abs logo thin">quorvane</div>
  <nav class="abs main-nav">
    <span style="left:256px">HOME</span>
    <span style="left:344px">WHO WE ARE</span>
    <span style="left:482px">WHAT WE DO</span>
    <span style="left:610px">OUR WORK</span>
    <span style="left:736px">OUR CLIENTS</span>
    <span style="left:882px">CONTACT</span>
  </nav>
</header>

<section class="abs intro">
  <h1 class="thin">At Quorvane we are healthcare communication specialists.<br>This means we're scientists, journalists<br>and marketers rolled into one.</h1>
  <p>As you can see we provide all the things you'd expect from a<br>top-class healthcare communications agency, but we have the<br>depth of technical understanding and creative flair to produce sophisticated and memorable materials and programs</p>
</section>
<div class="abs media" style="left:948px;top:232px;width:174px;height:194px" role="img" aria-label="Printed education brochures"></div>

<section class="abs who">
  <h2>WHO WE ARE</h2>
  <p class="team">All members of our in-house team of project managers,<br>medical writers, designers, administration and production staff<br>are dedicated to delivery on time, on budget, and beyond expectations.</p>
  <div class="abs portrait" role="img" aria-label="Portrait of the managing director"></div>
  <p class="name">GILES MARROW</p>
  <p class="role">Managing Director</p>
  <p class="bio">After graduating with honours from Harcourt University, UK, Giles entered the pharmaceutical industry as an information scientist. He soon moved into medical education and entered the competitive European healthcare communications marketplace. He worked for a number of healthcare education agencies in the UK before moving to Australia and setting up Quorvane in 2000.</p>
  <div class="abs proud-rule" style="top:117px"></div>
  <div class="abs proud thin">We are<br>proud<br>of what we do!</div>
  <div class="abs proud-rule" style="top:401px"></div>
</section>

<section class="abs what">
  <div class="top"></div>
  <h2>WHAT WE DO</h2>
  <div class="tabs">
    <span style="left:74px">PROMOTION</span>
    <span class="active" style="left:194px;width:112px;text-align:center">EDUCATION</span>
    <span style="left:330px">PROGRAMS</span>
    <span style="left:458px">MEETINGS</span>
    <span style="left:588px">IME</span>
  </div>
  <h3>EDUCATION</h3>
  <p>Clinical papers, evidence summaries, scientific newsletters and accredited educational materials are among the supporting materials we excel at. We pride ourselves on our ability to produce current, in-depth, credible educational and/or scientific material for a wide variety of audiences, from patients to key opinion leaders.</p>
  <svg class="abs" style="left:4px;top:230px" width="54" height="58" viewBox="0 0 54 58"><path d="M54 0 L0 29 L54 58 Z" fill="#bdbdbd"/></svg>
  <svg class="abs" style="left:1142px;top:230px" width="54" height="58" viewBox="0 0 54 58"><path d="M0 0 L54 29 L0 58 Z" fill="#bdbdbd"/></svg>
</section>
<div class="abs media" style="left:925px;top:1058px;width:177px;height:194px;background:linear-gradient(135deg,#f4f4f4,#d9c6df 50%,#f0f0f0)" role="img" aria-label="Education materials display"></div>

<section class="clients">
  <h2>WHAT OUR CLIENTS ARE SAYING</h2>
  <div class="abs quotes">
    <p>"Congratulations &amp; many thanks for your seriously wonderful &amp; successful work on the weekend. I'm especially grateful for the calm, cool &amp; very clever work done in managing all the planning processes before I even came on board – truly outstanding"</p>
    <p>"Thank you for all your help with making the meeting the huge success that it was"</p>
    <p>"I wanted to thank you for your work – I know you were thrown into the deep end with this meeting and also our sometimes unrealistic expectations you did a fantastic job! All the team know what a great job Quorvane do on these meetings"</p>
  </div>
  <div class="abs media" style="left:938px;top:1520px;width:177px;height:140px;background:linear-gradient(135deg,#f2f2f2,#e3c94c 40%,#3a8fb0 70%,#eee)" role="img" aria-label="Cardiovascular brochure"></div>
  <p class="abs some">SOME OF OUR CLIENTS</p>
  <div class="abs client" style="left:245px;top:1780px"><i></i>Veltrano</div>
  <div class="abs client" style="left:425px;top:1780px"><i></i>Corvix</div>
  <div class="abs client" style="left:690px;top:1774px"><i></i>Pennard</div>
  <div class="abs client" style="left:815px;top:1774px"><i></i>Strelvia</div>
  <div class="abs client" style="left:268px;top:1834px"><i></i>Halden</div>
  <div class="abs client" style="left:396px;top:1834px"><i></i>Morvell-Tane</div>
  <div class="abs client" style="left:666px;top:1840px"><i></i>Orlande Pharma</div>
  <div class="abs client" style="left:840px;top:1826px"><i></i>Kestrom</div>
</section>

<section class="abs join">
  <h2>JOIN NOW QUORVANE.NET.AU</h2>
  <p class="tag">Sign up for deals, news, and giveaways:</p>
  <div class="field">Email Address</div>
  <div class="btn">SUBSCRIBE</div>
</section>

<footer class="abs footer">
  <h2>CONTACT</h2>
  <h4 style="left:88px;top:78px">Address</h4>
  <p class="lines" style="left:88px;top:108px">Quorvane Healthcare Education<br>Level 4, 18 Calder Street<br>Westmere NSW 2071<br>Australia</p>
  <h4 style="left:352px;top:78px">Call Giles Marrow, Managing Director</h4>
  <p class="lines" style="left:352px;top:108px">Phone:&nbsp; +61 2 9000 4812<br>Facsimile:&nbsp; +61 2 9000 4813<br>Email: info@quorvane.net.au</p>
  <div class="social" style="left:784px"><i></i>LOOPA</div>
  <div class="social" style="left:840px"><i></i>CHATTERLY</div>
  <div class="social" style="left:896px"><i></i>GATHERLY</div>
  <div class="social" style="left:952px"><i></i>BOARDLY</div>
  <div class="social" style="left:1008px"><i></i>STREAMO</div>
  <p class="small" style="left:70px">©2013 QUORVANE.NET.AU. ALL RIGHTS RESERVED</p>
  <p class="small" style="left:1088px">SITEMAP</p>
</footer>

<div class="abs map" role="img" aria-label="Street map of the office location"></div>
<svg class="abs" style="left:586px;top:2405px" width="26" height="36" viewBox="0 0 26 36"><path d="M13 0 C5.8 0 0 5.8 0 13 C0 22 13 36 13 36 C13 36 26 22 26 13 C26 5.8 20.2 0 13 0 Z" fill="var(--brand-blue)"/></svg>

</body>
</html>
```